ulmar stationary etc..
Business Card, Stationary and Envelope Design
Please upload ai or eps of your logo.
The business cards need to be double sided
Hi sir,
I submitted my design please let the feedback and suggestions
Thank you
Veltrusa

```html
<!DOCTYPE html>
<html lang="en">
<head>
<meta charset="utf-8">
<title>ulmar Cloud Computing – Stationery Set</title>
<link href="https://fonts.googleapis.com/css2?family=Montserrat:wght@700;800&family=Open+Sans:wght@400;600&display=swap" rel="stylesheet">
<style>
  :root{
    --page:#ffffff;
    --edge:#c9ced6;
    --ink:#15233d;
    --sky-top:#8fb4e0;
    --sky-mid:#c6dbf1;
    --sky-low:#edf3fa;
    --band-deep:#0b3c8e;
    --band-mid:#1766c4;
    --band-light:#3a97e6;
    --band-rule:#16192a;
    --on-band:#e6f0ff;
  }
  *{box-sizing:border-box;margin:0;padding:0}
  html,body{width:1200px;height:737px;overflow:hidden;background:var(--page)}
  .canvas{position:relative;width:1200px;height:737px;background:var(--page);font-family:"Open Sans",Arial,sans-serif}

  .piece{position:absolute;overflow:hidden;border:1px solid var(--edge);background:var(--page)}
  .sky{position:absolute;left:0;top:0;width:100%;
    background:linear-gradient(180deg,var(--sky-top) 0%,var(--sky-mid) 45%,var(--sky-low) 100%);}
  .band{position:absolute;left:0;width:100%;
    background:linear-gradient(180deg,var(--band-deep) 0%,var(--band-mid) 55%,var(--band-light) 100%);
    border-top:6px solid var(--band-rule);
    color:var(--on-band);text-align:center;}

  .brand{position:absolute;text-align:center;line-height:1}
  .brand-name{font-family:"Montserrat",Arial,sans-serif;font-weight:800;color:var(--ink);letter-spacing:-1px}
  .brand-name .dot{display:inline-block;border-radius:50%;background:var(--band-mid);vertical-align:middle;margin-left:6px}
  .brand-tag{font-family:"Montserrat",Arial,sans-serif;font-weight:700;color:var(--ink);letter-spacing:2px}
  .brand.light .brand-name,.brand.light .brand-tag{color:#fff}
  .brand.light .brand-name .dot{background:#fff}

  .small{font-size:8.5px;line-height:12px}

  /* letterhead */
  .letterhead{left:29px;top:19px;width:528px;height:696px}
  .letterhead .sky{height:100%}
  .letterhead .brand{left:0;width:100%;top:22px}
  .letterhead .brand-name{font-size:50px}
  .letterhead .brand-name .dot{width:12px;height:12px}
  .letterhead .brand-tag{font-size:11px;margin-top:4px}
  .letterhead .band{top:620px;height:76px;padding:8px 40px 0 180px}

  /* envelope front */
  .envelope-front{left:583px;top:19px;width:593px;height:262px}
  .envelope-front .sky{height:100%}
  .envelope-front .brand{left:12px;top:18px;width:200px}
  .envelope-front .brand-name{font-size:44px}
  .envelope-front .brand-name .dot{width:10px;height:10px}
  .envelope-front .brand-tag{font-size:10px;margin-top:3px}
  .envelope-front .band{top:193px;height:69px;padding-top:14px;text-align:left;padding-left:150px}

  /* envelope back */
  .envelope-back{left:583px;top:305px;width:593px;height:252px}
  .envelope-back svg{position:absolute;left:0;top:0}
  .envelope-back .brand{left:0;width:100%;top:40px}
  .envelope-back .brand-name{font-size:36px}
  .envelope-back .brand-name .dot{width:8px;height:8px}
  .envelope-back .brand-tag{font-size:8px;margin-top:3px}

  /* business card front */
  .card-front{left:583px;top:583px;width:221px;height:127px}
  .card-front .sky{height:100%}
  .card-front .brand{left:0;width:100%;top:8px}
  .card-front .brand-name{font-size:30px}
  .card-front .brand-name .dot{width:7px;height:7px;margin-left:4px}
  .card-front .brand-tag{font-size:7px;margin-top:2px;letter-spacing:1.5px}
  .card-front .band{top:55px;height:72px;padding-top:3px}
  .card-name{font-size:9px;font-weight:600;line-height:11px}
  .card-front .small{font-size:7px;line-height:9px}

  /* business card back */
  .card-back{left:847px;top:583px;width:219px;height:127px;
    background:radial-gradient(ellipse 45% 55% at 45% 45%,#6ab7f5 0%,var(--band-mid) 45%,var(--band-deep) 100%)}
  .card-back .brand{left:0;width:100%;top:36px}
  .card-back .brand-name{font-size:30px}
  .card-back .brand-name .dot{width:7px;height:7px;margin-left:4px}
  .card-back .brand-tag{font-size:7px;margin-top:2px;letter-spacing:1.5px}
  .card-back .web{position:absolute;left:0;bottom:0;width:100%;height:14px;background:var(--band-rule);
    color:var(--on-band);font-size:7px;line-height:14px;text-align:center}
</style>
</head>
<body>
<main class="canvas">

  <section class="piece letterhead" aria-label="Letterhead">
    <div class="sky" role="img" aria-label="Photo of a blue sky with white clouds"></div>
    <div class="brand">
      <div class="brand-name">ulmar<span class="dot"></span></div>
      <div class="brand-tag">CLOUD COMPUTING</div>
    </div>
    <footer class="band small">
      <p>48 Harbor Lane, Fernvale, NJ 07911</p>
      <p>Toll Free: 1 800 555 0142 (INFO) | Phone: 1 201 555 0190 Ext. 908</p>
      <p>Email: hello@ulmar.net | www.ulmar.net</p>
    </footer>
  </section>

  <section class="piece envelope-front" aria-label="Envelope front">
    <div class="sky" role="img" aria-label="Photo of a blue sky with white clouds"></div>
    <div class="brand">
      <div class="brand-name">ulmar<span class="dot"></span></div>
      <div class="brand-tag">CLOUD COMPUTING</div>
    </div>
    <footer class="band small"><p>48 Harbor Lane, Fernvale, NJ 07911</p></footer>
  </section>

  <section class="piece envelope-back" aria-label="Envelope back">
    <svg width="593" height="252" viewBox="0 0 593 252" aria-hidden="true">
      <defs>
        <linearGradient id="flapFill" x1="0" y1="0" x2="0" y2="1">
          <stop offset="0" stop-color="#0b3c8e"/>
          <stop offset=".6" stop-color="#1766c4"/>
          <stop offset="1" stop-color="#3a97e6"/>
        </linearGradient>
      </defs>
      <path d="M0 0 H593 V82 Q296 128 0 82 Z" fill="url(#flapFill)"/>
    </svg>
    <div class="brand light">
      <div class="brand-name">ulmar<span class="dot"></span></div>
      <div class="brand-tag">CLOUD COMPUTING</div>
    </div>
  </section>

  <section class="piece card-front" aria-label="Business card front">
    <div class="sky" role="img" aria-label="Photo of a blue sky with white clouds"></div>
    <div class="brand">
      <div class="brand-name">ulmar<span class="dot"></span></div>
      <div class="brand-tag">CLOUD COMPUTING</div>
    </div>
    <div class="band">
      <p class="card-name">Rena Sollis</p>
      <p class="small">Founder</p>
      <p class="small">48 Harbor Lane, Fernvale, NJ 07911</p>
      <p class="small">Toll Free: 1 800 555 0142</p>
      <p class="small">Phone: 1 201 555 0190 Ext. 908</p>
      <p class="small">hello@ulmar.net</p>
    </div>
  </section>

  <section class="piece card-back" aria-label="Business card back">
    <div class="brand light">
      <div class="brand-name">ulmar<span class="dot"></span></div>
      <div class="brand-tag">CLOUD COMPUTING</div>
    </div>
    <p class="web">www.ulmar.net</p>
  </section>

</main>
</body>
</html>
```